Update New Business Card - For Start Up

I need to update my business card, I have our old version for example. I would like to keep to the same colors and theme. We are a threat reporting and case management tool for corporations and educational institutions.

Target Market(s)

Corporate Security and Human Resources, School Administrators and Superintendents.

Industry/Entity Type

Physical Security and Technology.

Contact Information for Business Card

My Name, Founder/CEO, phone number 777-412-5068, Logo, Web...

Colors
0054AA
0677BA
7BADD7
CADEEF
E8F1F8

Requirements
Must have
• Something new and trendy.

```html
<!DOCTYPE html>
<html lang="en">
<head>
<meta charset="utf-8">
<title>Vigilora Business Card</title>
<link href="https://fonts.googleapis.com/css2?family=Montserrat:wght@400;500;700&display=swap" rel="stylesheet">
<style>
  :root {
    --brand-blue: #1b75bc;
    --deep-blue: #0054aa;
    --ink: #1f1f1f;
    --paper: #ffffff;
    --canvas: #eef0f2;
    --edge: #c9ccd1;
  }
  * { margin: 0; padding: 0; box-sizing: border-box; }
  html, body {
    width: 1058px;
    height: 1200px;
    overflow: hidden;
    background: var(--canvas);
    font-family: "Montserrat", sans-serif;
  }
  .sheet {
    width: 1058px;
    height: 1200px;
    display: flex;
    flex-direction: column;
    align-items: center;
    justify-content: center;
    gap: 70px;
  }
  .card {
    position: relative;
    width: 880px;
    height: 495px;
    overflow: hidden;
  }
  .card-back {
    background: var(--brand-blue);
    display: flex;
    align-items: center;
    justify-content: center;
    gap: 20px;
  }
  .card-back .brand-dot {
    width: 64px;
    height: 64px;
    border-radius: 50%;
    background: var(--paper);
  }
  .card-back .brand-name {
    color: var(--paper);
    font-weight: 500;
    font-size: 44px;
    letter-spacing: 6px;
  }
  .card-front {
    background: var(--paper);
    border: 1px solid var(--edge);
  }
  .brand {
    position: absolute;
    top: 48px;
    left: 0;
    right: 0;
    display: flex;
    align-items: center;
    justify-content: center;
    gap: 14px;
  }
  .brand-mark {
    width: 46px;
    height: 46px;
    border-radius: 50%;
    background: var(--brand-blue);
  }
  .brand .brand-name {
    color: var(--brand-blue);
    font-weight: 500;
    font-size: 38px;
    letter-spacing: 5px;
  }
  .person {
    position: absolute;
    top: 182px;
    left: 0;
    right: 0;
    text-align: center;
  }
  .person-name {
    color: var(--brand-blue);
    font-weight: 700;
    font-size: 28px;
    letter-spacing: 0.5px;
  }
  .person-title {
    margin-top: 8px;
    color: var(--ink);
    font-weight: 500;
    font-size: 18px;
    letter-spacing: 4px;
  }
  .side-bar {
    position: absolute;
    top: 110px;
    width: 27px;
    height: 212px;
    background: var(--brand-blue);
  }
  .side-bar.left { left: 0; }
  .side-bar.right { right: 0; }
  .divider {
    position: absolute;
    top: 341px;
    width: 3px;
    height: 126px;
    background: var(--brand-blue);
  }
  .divider.first { left: 269px; }
  .divider.second { left: 571px; }
  .contact {
    position: absolute;
    top: 360px;
    width: 280px;
    text-align: center;
    color: var(--ink);
    font-size: 21px;
    line-height: 33px;
  }
  .contact svg {
    display: block;
    margin: 0 auto 12px;
    width: 24px;
    height: 24px;
    fill: var(--brand-blue);
  }
  .contact.phone { left: -8px; }
  .contact.email { left: 278px; }
  .contact.web { left: 589px; }
</style>
</head>
<body>
<main class="sheet">
  <section class="card card-back">
    <span class="brand-dot"></span>
    <span class="brand-name">VIGILORA</span>
  </section>

  <section class="card card-front">
    <div class="brand">
      <span class="brand-mark"></span>
      <span class="brand-name">VIGILORA</span>
    </div>

    <div class="person">
      <p class="person-name">DANA WHITFIELD</p>
      <p class="person-title">CHIEF EXECUTIVE OFFICER</p>
    </div>

    <span class="side-bar left"></span>
    <span class="side-bar right"></span>
    <span class="divider first"></span>
    <span class="divider second"></span>

    <div class="contact phone">
      <svg viewBox="0 0 24 24" aria-hidden="true"><path d="M6.6 10.8a15.1 15.1 0 0 0 6.6 6.6l2.2-2.2a1 1 0 0 1 1-.25 11.4 11.4 0 0 0 3.6.57 1 1 0 0 1 1 1V20a1 1 0 0 1-1 1A17 17 0 0 1 3 4a1 1 0 0 1 1-1h3.5a1 1 0 0 1 1 1c0 1.25.2 2.45.57 3.57a1 1 0 0 1-.25 1z"/></svg>
      <p>888-899-3799</p>
      <p>777-412-5068</p>
    </div>

    <div class="contact email">
      <svg viewBox="0 0 24 24" aria-hidden="true"><path d="M2 5h20v14H2z M3.5 6.5 12 12.5l8.5-6" fill="none" stroke="#1b75bc" stroke-width="0"/><path d="M2 5h20v2l-10 6L2 7z"/><path d="M2 9l10 6 10-6v10H2z"/></svg>
      <p>dana@vigilora.co</p>
    </div>

    <div class="contact web">
      <svg viewBox="0 0 24 24" aria-hidden="true"><path d="M12 2a10 10 0 1 0 0 20 10 10 0 0 0 0-20zm6.9 6h-2.9a15.6 15.6 0 0 0-1.4-3.6A8 8 0 0 1 18.9 8zM12 4c.8 1.2 1.5 2.5 1.9 4h-3.8c.4-1.5 1.1-2.8 1.9-4zM4.3 14a8 8 0 0 1 0-4h3.4a16 16 0 0 0 0 4zm.8 2h2.9c.3 1.3.8 2.5 1.4 3.6A8 8 0 0 1 5.1 16zM8 8H5.1a8 8 0 0 1 4.3-3.6C8.8 5.5 8.3 6.7 8 8zm4 12c-.8-1.2-1.5-2.5-1.9-4h3.8c-.4 1.5-1.1 2.8-1.9 4zm2.3-6H9.7a14.5 14.5 0 0 1 0-4h4.6a14.5 14.5 0 0 1 0 4zm.3 5.6c.6-1.1 1.1-2.3 1.4-3.6h2.9a8 8 0 0 1-4.3 3.6zm1.7-5.6a16 16 0 0 0 0-4h3.4a8 8 0 0 1 0 4z"/></svg>
      <p>www.vigilora.co</p>
    </div>
  </section>
</main>
</body>
</html>
```